Documentary Movie Needs a Poster

We need a poster/lobby card for a documentary film made by six filmmakers. Lobby card needs to list name of sponsor, names of filmmakers and (if feasible, but not required) image frames from each of the six sections of the film.

Text should be very readable. OK to have all caps text or upper/lower.

Design comps are OK, these do not need to be print-ready final images.

Target Market(s)

well educated documentary filmgoers

Industry/Entity Type

Movie

Requirements
Must have
• Must contain the following text (please use helvetica neue or similar font).

Please use the following sponsor name:

The
Harwell Center for Filmmaking
presents

Please use the following filmmaker names:

Theodore Marsouli
Patrick Ennis
Raymond Hollowell
Samuel R. T. Vorne
Oliver Prescott
Danny Rusk

Please use the 6 images in archive/zip to create the card.

You can also do text-only versions of the card (no images).

Card needs to be 2:1 aspect ratio (2000px wide x 1000 pixels high)

Names of filmmakers should each be same size (no filmmaker has visual priority over the other).

Colors for text, lines and other design elements should be RED, BLACK and/or WHITE.

Feel free to crop images if you need to.

```html
<!DOCTYPE html>
<html lang="en">
<head>
<meta charset="utf-8">
<title>Harwell Center for Filmmaking Presents</title>
<link rel="stylesheet" href="https://fonts.googleapis.com/css2?family=Inter:wght@200;300;900&display=swap">
<style>
  :root {
    --card-red: #d2232a;
    --band-white: #fbf1ea;
    --ink-black: #0b0b0b;
    --paper-white: #ffffff;
  }
  * { margin: 0; padding: 0; box-sizing: border-box; }
  html, body {
    width: 1200px;
    height: 600px;
    overflow: hidden;
    background: var(--card-red);
  }
  .lobby-card {
    position: relative;
    width: 1200px;
    height: 600px;
    background: var(--card-red);
    font-family: "Inter", "Helvetica Neue", Helvetica, Arial, sans-serif;
    overflow: hidden;
  }
  .sponsor-line {
    position: absolute;
    top: 22px;
    left: 0;
    width: 100%;
    text-align: center;
    color: var(--paper-white);
    font-weight: 300;
    font-size: 26px;
    letter-spacing: 3.5px;
    text-transform: uppercase;
    line-height: 1;
  }
  .sponsor-line .minor { font-size: 20px; }

  .band {
    position: absolute;
    height: 70px;
  }
  .band--fade-right {
    background: linear-gradient(to right, var(--band-white) 0%, var(--band-white) 8%, var(--card-red) 100%);
  }
  .band--fade-left {
    background: linear-gradient(to right, var(--card-red) 0%, var(--band-white) 100%);
  }

  .filmmaker {
    position: absolute;
    display: flex;
    align-items: baseline;
    gap: 22px;
    white-space: nowrap;
    text-transform: uppercase;
    line-height: 1;
  }
  .filmmaker__given {
    font-weight: 900;
    font-size: 42px;
    color: var(--ink-black);
    letter-spacing: 0.5px;
  }
  .filmmaker__family {
    font-weight: 200;
    font-size: 84px;
    color: var(--paper-white);
    letter-spacing: -1px;
  }
</style>
</head>
<body>
  <main class="lobby-card">
    <p class="sponsor-line"><span class="minor">The</span> Harwell Center <span class="minor">for</span> Filmmaking Presents</p>

    <div class="band band--fade-right" style="top:95px; left:0; width:280px;"></div>
    <div class="band band--fade-left" style="top:170px; left:560px; width:640px;"></div>
    <div class="band band--fade-right" style="top:258px; left:0; width:370px;"></div>
    <div class="band band--fade-right" style="top:342px; left:0; width:430px;"></div>
    <div class="band band--fade-left" style="top:425px; left:690px; width:510px;"></div>
    <div class="band band--fade-right" style="top:510px; left:0; width:410px;"></div>

    <div class="filmmaker" style="top:91px; left:70px;">
      <span class="filmmaker__given">Theodore</span>
      <span class="filmmaker__family">Marsouli</span>
    </div>
    <div class="filmmaker" style="top:166px; left:535px;">
      <span class="filmmaker__given">Patrick</span>
      <span class="filmmaker__family">Ennis</span>
    </div>
    <div class="filmmaker" style="top:254px; left:100px;">
      <span class="filmmaker__given">Raymond</span>
      <span class="filmmaker__family">Hollowell</span>
    </div>
    <div class="filmmaker" style="top:338px; left:190px;">
      <span class="filmmaker__given">Samuel R. T.</span>
      <span class="filmmaker__family">Vorne</span>
    </div>
    <div class="filmmaker" style="top:421px; left:430px;">
      <span class="filmmaker__given">Oliver</span>
      <span class="filmmaker__family">Prescott</span>
    </div>
    <div class="filmmaker" style="top:506px; left:120px;">
      <span class="filmmaker__given">Danny</span>
      <span class="filmmaker__family">Rusk</span>
    </div>
  </main>
</body>
</html>
```